Maplerise Trading Inc. needs an innovative idea for letterhead and visiting cards.

Maplerise Trading Inc. is a Canadian brand since 2007. It is a renown dealer of kids and office furniture locally. Moreover, exporting electric fixtures e.g. switches, LED's, down-lights etc. to Middle East and Africa. We have initiated a number of steps including re-branding, to boost our export in 2020. We have successfully designed our new logo a few months ago through 'Artfolio' and now we are looking for an innovative idea for a letterhead.
Some key points:
• Red, black and white are the three colors used in all our packaging and furniture. (grey is optional)
• Shouldn’t be too wide.
• Use of watermark is preferable.
• You can visit our North American site at www.mapleriseinc.com. Export website of the company will be launched soon. www.mapleriseinc.ca
• Same letterhead will be used locally and internationally.
• Our new logo and sample packaging is attached.

```html
<!DOCTYPE html>
<html lang="en">
<head>
<meta charset="utf-8">
<title>Maplerise Trading – Letterhead</title>
<link href="https://fonts.googleapis.com/css2?family=Roboto:wght@300;400&display=swap" rel="stylesheet">
<style>
  :root{
    --brand-red:#a50f16;
    --ink:#4a4a4a;
    --ink-soft:#5f5f5f;
    --paper:#ffffff;
    --paper-shade:#f1f1f1;
    --backdrop:#e2e2e2;
  }
  *{box-sizing:border-box;margin:0;padding:0}
  html,body{width:1200px;height:1141px;overflow:hidden;background:var(--backdrop)}
  body{font-family:"Roboto",sans-serif;color:var(--ink);position:relative}
  .letterhead{
    position:absolute;left:208px;top:20px;width:783px;height:1101px;
    background:linear-gradient(160deg,var(--paper) 40%,var(--paper-shade) 100%);
    box-shadow:0 2px 6px rgba(0,0,0,.18);
  }
  .brand{
    position:absolute;top:110px;left:0;right:0;
    display:flex;justify-content:center;align-items:center;gap:10px;
  }
  .brand-mark{width:22px;height:22px;background:var(--brand-red)}
  .brand-name{font-weight:400;font-size:27px;color:var(--brand-red);letter-spacing:.5px}
  .salutation{
    position:absolute;left:70px;top:276px;font-size:20px;font-weight:400;color:var(--ink-soft);
  }
  .letter-body{
    position:absolute;left:70px;top:327px;width:643px;
    font-size:11.2px;font-weight:300;line-height:16.8px;text-align:justify;color:var(--ink);
  }
  .letter-body p{margin-bottom:16.5px}
  .closing{position:absolute;left:70px;top:717px;font-size:11.5px;font-weight:300}
  .signature{
    position:absolute;left:61px;top:753px;width:172px;height:70px;
    background:linear-gradient(90deg,rgba(30,30,30,.08),rgba(30,30,30,.03));border-radius:4px;
  }
  .contact{
    position:absolute;left:66px;top:1004px;font-size:12.2px;font-weight:400;color:var(--ink);
  }
  .contact li{list-style:none;display:flex;align-items:center;gap:7px;height:16.3px}
  .contact svg{width:10px;height:10px;fill:var(--brand-red)}
  .divider{position:absolute;left:256px;top:1004px;width:1px;height:48px;background:var(--brand-red)}
  .address{
    position:absolute;left:272px;top:1022px;font-size:12.2px;line-height:15.5px;color:var(--ink);
  }
</style>
</head>
<body>
<main class="letterhead">
  <header class="brand">
    <span class="brand-mark"></span>
    <span class="brand-name">MAPLERISE TRADING</span>
  </header>

  <h1 class="salutation">Dear Mr. Hartley,</h1>

  <section class="letter-body">
    <p>Lorem ipsum dolor sit amet, consectetur adipiscing elit. Donec orci purus, luctus vitae dignissim eu, iaculis sed purus. Vivamus faucibus, ipsum nec aliquet viverra, leo mauris condimentum ligula, sit amet sagittis enim ligula quis arcu. Nam egestas tortor id nisi porttitor mattis. In tortor ante, ultricies in suscipit a, tempus non massa. Vivamus et auctor mi. Fusce vel massa nulla. Phasellus nec eros mauris, et scelerisque orci.</p>
    <p>Donec malesuada orci vitae nulla accumsan porta a id massa. Quisque accumsan iaculis magna sit amet fringilla. Maecenas consequat, magna eget tincidunt semper, odio nibh rutrum mi, id feugiat ante nisi eu risus. Vestibulum nunc orci, rhoncus a placerat in, ultricies in mi. Cras mattis varius eros, vel fringilla nisi suscipit eget. Quisque scelerisque sagittis nulla at porttitor.</p>
    <p>Sed id augue vitae urna euismod commodo aliquet a quam. Pellentesque arcu velit, cursus et malesuada ut, consequat et diam. Nullam erat sem, rhoncus id ullamcorper vitae, rhoncus et arcu. In ultricies ultricies nulla, ut rutrum nisi iaculis at. Donec eu magna a metus ornare faucibus. Fusce aliquet faucibus ultricies. Morbi semper, est id tincidunt gravida, sem arcu adipiscing lacus, ac bibendum nulla leo eu purus. Quisque nec diam sed risus consectetur a ccumsan quis quis nibh. Vestibulum id purus lorem.</p>
    <p>It is a long established fact that a reader will be distracted by the readable content of a page when looking at its layout. The point of using Lorem Ipsum is that it has a more-or-less normal distribution of letters, as opposed to using 'Content here, content here', making it look like readable English. Many desktop publishing packages</p>
    <p>ada ut, consequat et diam. Nullam erat sem, rhoncus id ullamcorper vitae, rhoncus et arcu. In ultricies ultricies nulla, ut rutrum nisi iaculis at. Donec eu magna a metus ornare faucibus. Fusce aliquet faucibus ultricies. Morbi semper,</p>
  </section>

  <p class="closing">Sincerely,</p>
  <div class="signature" role="img" aria-label="Handwritten signature of the sender"></div>

  <ul class="contact">
    <li><svg viewBox="0 0 10 10"><path d="M2 0.5 L3.6 2.6 L2.8 3.6 Q4 6 6.4 7.2 L7.4 6.4 L9.5 8 L8.4 9.5 Q4.5 9.5 0.5 1.6 Z"/></svg>+1 (888) 420-3176</li>
    <li><svg viewBox="0 0 10 10"><path d="M0 2 H10 V8.5 H0 Z M0.6 2.4 L5 5.6 L9.4 2.4" stroke="#fff" stroke-width="0.8"/></svg>sales@mapleriseinc.com</li>
    <li><svg viewBox="0 0 10 10"><circle cx="5" cy="5" r="4.8"/><path d="M2 3.2 Q4 2.2 4.6 4 Q3.6 5.6 5 7 Q6.8 6.2 7.8 4.2" fill="none" stroke="#fff" stroke-width="0.9"/></svg>www.mapleriseinc.com</li>
  </ul>
  <div class="divider"></div>
  <address class="address" style="font-style:normal">48 Alder Crest Rd,<br>Unit 210, Oakridge Hill</address>
</main>
</body>
</html>
```